Lorne Hollow Farm Postcard Design

I am looking for a new postcard design to mail out this season. We are a Farm business that does wholesale and retail and bulk seasoned firewood sales. we sell firewood from anything from bagged wood to tractor trailer loads of wood. We sell firewood in bulk bags. Pick up or delivery available there is no order to big or too small. I need my business name and phone number on the cards Lorne Hollow Farm 848-316-0572 (call or text) I would like it to say we are the best priced guaranteed. I want something that is simple and straight forward but also really catches the eye when they see these in the mail box. I attached my logo and feel free to use photos of split firewood if you would like. id like my email on the card Lornehollowfarm90@mailvista.net.

Target Market(s)

Firewood purchasers

Industry/Entity Type

agriculture

Requirements
Must have
• email phone number logo

```html
<!DOCTYPE html>
<html lang="en">
<head>
<meta charset="utf-8">
<title>Lorne Hollow Farm Postcard</title>
<link href="https://fonts.googleapis.com/css2?family=Mulish:wght@400;700;900&display=swap" rel="stylesheet">
<style>
  :root {
    --backdrop: #a9a9a9;
    --ink: #0c0c0c;
    --paper: #ffffff;
    --flame-red: #e8432a;
    --flame-orange: #f6921e;
    --flame-yellow: #fcc419;
    --forest: #3b5a2a;
    --grass: #4f8a34;
    --wood: #a0673a;
  }
  html, body {
    margin: 0;
    width: 1199px;
    height: 1200px;
    overflow: hidden;
    background: var(--backdrop);
    font-family: "Mulish", Arial, sans-serif;
  }
  .postcard {
    position: absolute;
    left: 204px;
    width: 790px;
    height: 526px;
    display: block;
  }
  .postcard--front { top: 42px; }
  .postcard--back { top: 627px; }
  .headline { font-weight: 900; letter-spacing: -0.5px; }
  .brand-name { font-weight: 900; }
  .contact-phone { font-weight: 900; }
  .contact-email { font-weight: 400; }
  .promise { font-weight: 700; }
</style>
</head>
<body>

<!-- Front of postcard -->
<svg class="postcard postcard--front" viewBox="0 0 633 421" xmlns="http://www.w3.org/2000/svg">
  <defs>
    <linearGradient id="scene-tone" x1="0" y1="0" x2="0" y2="1">
      <stop offset="0" stop-color="var(--forest)"/>
      <stop offset="0.6" stop-color="#6b5236"/>
      <stop offset="0.78" stop-color="var(--wood)"/>
      <stop offset="0.82" stop-color="var(--grass)"/>
      <stop offset="1" stop-color="#3f7a2a"/>
    </linearGradient>
    <linearGradient id="panel-glow" x1="0" y1="0" x2="0.3" y2="1">
      <stop offset="0" stop-color="#f8a21f" stop-opacity="0.95"/>
      <stop offset="0.5" stop-color="var(--flame-yellow)" stop-opacity="0.9"/>
      <stop offset="1" stop-color="var(--flame-orange)" stop-opacity="0.9"/>
    </linearGradient>
  </defs>

  <rect class="photo-area" width="633" height="421" fill="url(#scene-tone)" role="img" aria-label="Photo of stacked split firewood beside a tractor and log splitter on grass in front of trees"/>

  <path class="feature-panel" d="M48 0 H387 V300 Q300 380 190 400 Q80 410 48 300 Z" fill="url(#panel-glow)"/>

  <path class="contact-band" d="M350 315 H633 V375 H350 Z" fill="var(--ink)"/>
  <path class="promise-swoop" d="M140 390 Q200 300 330 288 Q380 286 360 315 L350 375 Q250 380 140 390 Z" fill="var(--ink)"/>

  <text class="headline" fill="var(--ink)" font-size="45">
    <tspan x="88" y="117">BULK</tspan>
    <tspan x="88" y="160">SEASONED</tspan>
    <tspan x="88" y="202">FIREWOOD</tspan>
    <tspan x="88" y="245">SALES</tspan>
  </text>

  <g class="promise" fill="var(--paper)" font-size="13.5" text-anchor="middle">
    <text x="247" y="326">Best Price</text>
    <text x="247" y="344">Guaranteed</text>
  </g>

  <g class="brand-mark">
    <rect x="462" y="34" width="140" height="119" fill="var(--ink)"/>
    <text class="brand-name" x="532" y="90" fill="var(--flame-orange)" font-size="16" text-anchor="middle">Lorne Hollow</text>
    <text class="brand-name" x="532" y="110" fill="var(--flame-orange)" font-size="16" text-anchor="middle">Farm</text>
  </g>

  <text class="contact-phone" x="490" y="343" fill="var(--paper)" font-size="21" text-anchor="middle">848-316-0572</text>
  <text class="contact-email" x="490" y="365" fill="var(--paper)" font-size="11" text-anchor="middle">Lornehollowfarm90@mailvista.net</text>
</svg>

<!-- Back of postcard -->
<svg class="postcard postcard--back" viewBox="0 0 633 421" xmlns="http://www.w3.org/2000/svg">
  <defs>
    <linearGradient id="flame-fill" x1="0" y1="0" x2="1" y2="0">
      <stop offset="0" stop-color="var(--flame-red)"/>
      <stop offset="0.5" stop-color="var(--flame-orange)"/>
      <stop offset="1" stop-color="var(--flame-yellow)"/>
    </linearGradient>
    <clipPath id="card-edge"><rect width="633" height="421"/></clipPath>
  </defs>

  <rect width="633" height="421" fill="var(--paper)"/>
  <path class="dark-panel" d="M0 0 H337 V280 Q330 360 282 421 H0 Z" fill="var(--ink)"/>
  <circle class="flame-disc" cx="144" cy="363" r="165" fill="url(#flame-fill)" clip-path="url(#card-edge)"/>

  <text class="headline" fill="var(--paper)" font-size="29">
    <tspan x="40" y="78">BULK</tspan>
    <tspan x="40" y="106">SEASONED</tspan>
    <tspan x="40" y="135">FIREWOOD</tspan>
    <tspan x="40" y="163">SALES</tspan>
  </text>

  <g class="brand-mark">
    <text class="brand-name" x="287" y="70" fill="var(--flame-orange)" font-size="12" text-anchor="middle">Lorne Hollow</text>
    <text class="brand-name" x="287" y="86" fill="var(--flame-orange)" font-size="12" text-anchor="middle">Farm</text>
  </g>

  <text class="contact-phone" x="63" y="292" fill="var(--ink)" font-size="22">848-316-0572</text>
  <text class="contact-email" x="63" y="312" fill="var(--ink)" font-size="10.5">Lornehollowfarm90@mailvista.net</text>

  <rect class="stamp-box" x="500" y="43" width="88" height="98" fill="none" stroke="var(--ink)" stroke-width="1.5"/>
  <g class="address-lines" stroke="var(--ink)" stroke-width="1">
    <line x1="354" y1="256" x2="588" y2="256"/>
    <line x1="354" y1="302" x2="588" y2="302"/>
    <line x1="354" y1="348" x2="588" y2="348"/>
  </g>
</svg>

</body>
</html>
```